Pelmora Tours - Astronomy in the Kimberley

Pelmora Tours requires a web page to advertise astronomy tours in the East Kimberley, Australia. It needs the following tabs - Home, Tours, Astronomy Events, Gallery, Testimonials, Contacts.

It should target tourists to the Kimberley.
We are unsure of which colours to go with at the moment but we have included our logo if it helps.

It should be mobile and tablet friendly.

Target Market(s)

Families, +40, Tourist, hobby astronomists,

Industry/Entity Type

Events

Number of Pages Required

3 page

Colors
3377b5
ffffff

Requirements
Must have
• Home, Tours, Astronomy Events, Gallery, Calendar, Testimonials, Contacts.
• 'Pelmora Tours' logo
Nice to have
• Pictures of portable amateur telescopes. Pictures of Lake Kununurra or Wyndham.
Should not have
• Pictures of extremely large professional telescopes.

```html
<!DOCTYPE html>
<html lang="en">
<head>
<meta charset="utf-8">
<title>Pelmora Tours – Astronomy in the Kimberley</title>
<link rel="stylesheet" href="https://fonts.googleapis.com/css2?family=Exo+2:wght@400;500;600&family=Open+Sans:wght@400;600&display=swap">
<style>
:root{
  --blue:#3377b5;
  --blue-dark:#24609c;
  --blue-deep:#1b4a7d;
  --navy:#0f2748;
  --white:#ffffff;
  --ink:#3a3f47;
  --muted:#7b8490;
  --grey:#e9ecef;
  --footer:#1d1f24;
  --footer-bar:#141518;
  --orange:#f0a23a;
}
*{box-sizing:border-box;margin:0;padding:0}
html,body{width:1200px;height:2196px;overflow:hidden}
body{font-family:"Open Sans",Arial,sans-serif;color:var(--ink);background:var(--white);font-size:13px;line-height:1.5}
h1,h2,h3,.brand,.nav a,.btn{font-family:"Exo 2","Trebuchet MS",sans-serif}
a{color:inherit;text-decoration:none}

/* header */
.site-header{height:56px;display:flex;align-items:center;padding:0 40px;background:var(--white);border-bottom:1px solid var(--grey);white-space:nowrap}
.brand{display:flex;align-items:center;gap:10px;font-size:20px;font-weight:600;color:var(--blue);white-space:nowrap}
.brand-dot{width:22px;height:22px;border-radius:50%;background:var(--blue);flex:0 0 22px}
.nav{display:flex;gap:2px;margin-left:40px}
.nav a{font-size:13px;color:var(--blue);padding:5px 10px;border-radius:3px;white-space:nowrap;border:1px solid transparent}
.nav a.active{border-color:var(--blue)}
.header-meta{margin-left:auto;display:flex;align-items:center;gap:10px;font-size:11px;color:var(--muted);white-space:nowrap}
.header-meta .btn-sm{border:1px solid #c7ced6;padding:4px 10px;border-radius:3px;color:var(--ink);font-weight:600}

/* hero */
.hero{position:relative;height:484px;background:linear-gradient(180deg,#0b1830 0%,#1f3f6c 45%,#3f6da1 68%,#b36a3a 78%,#1b2a3d 86%,#0a1220 100%);color:var(--white);text-align:center}
.hero-weather{position:absolute;top:10px;right:40px;display:flex;align-items:center;gap:14px;font-size:11px;text-align:left;line-height:1.4}
.hero-weather strong{font-size:26px;font-family:"Exo 2",sans-serif;font-weight:500}
.hero h1{font-size:48px;font-weight:400;padding-top:150px}
.hero p{font-size:28px;font-family:"Exo 2",sans-serif;margin-top:2px}
.hero .btn{display:inline-block;margin-top:30px;border:2px solid var(--white);padding:12px 34px;font-size:18px}

/* welcome */
.welcome{height:300px;text-align:center;padding:44px 120px 0}
.welcome .logo-mark{width:54px;height:54px;border-radius:50%;background:var(--blue);margin:0 auto 10px}
.welcome .logo-name{font-family:"Exo 2",sans-serif;font-size:18px;font-weight:600;color:var(--blue);margin-bottom:14px}
.welcome h2{font-size:28px;font-weight:400;color:var(--blue);margin-bottom:10px}
.welcome p{font-size:13px;color:var(--muted)}

/* grid */
.grid{display:grid;grid-template-columns:repeat(3,400px);grid-template-rows:396px 324px 352px}
.tile{position:relative;padding:22px 24px;overflow:hidden}
.tile h3{font-size:26px;font-weight:400;margin-bottom:12px}
.tile .more{position:absolute;right:24px;bottom:16px;font-size:14px}
.t-blue{background:var(--blue);color:var(--white)}
.t-dark{background:var(--blue-dark);color:var(--white)}
.t-white{background:var(--white);color:var(--ink)}
.t-white h3{color:var(--blue)}
.t-grey{background:var(--grey)}
.t-grey h3{color:var(--blue)}

.calendar{background:var(--white);color:var(--ink);margin:0 -24px;padding:10px 24px}
.calendar .month{font-size:12px;font-weight:600;margin-bottom:4px}
.days{display:flex;justify-content:space-between;text-align:center}
.days div{width:44px;font-family:"Exo 2",sans-serif;font-size:22px;line-height:1.1;padding:4px 0}
.days span{display:block;font-size:10px;color:var(--muted)}
.days .today{background:var(--navy);color:var(--white)}
.days .today span{color:#9fb4cc}
.event-item{display:flex;gap:14px;margin-top:18px;font-size:12px}
.thumb{flex:0 0 80px;height:80px;border-radius:50%}
.thumb-night{background:radial-gradient(circle at 40% 40%,#5d86b7,#16325a)}

.rental{display:flex}
.rental .price-col{flex:1}
.rental .label{font-size:12px;color:var(--muted)}
.rental .price{font-family:"Exo 2",sans-serif;font-size:46px;color:var(--orange);line-height:1;white-space:nowrap}
.rental .price small{font-size:14px;color:var(--muted)}
.rental p{font-size:12px;color:var(--muted);margin-top:10px}
.rental .product{width:150px;height:230px;background:linear-gradient(180deg,#ffffff,#eef1f4)}

.weather-now{display:flex;align-items:center;gap:18px}
.weather-now .temp{font-family:"Exo 2",sans-serif;font-size:44px;line-height:1}
.weather-now .place{font-size:12px;text-align:right;margin-left:auto}
.moon{margin-top:16px;font-size:14px}
.phases{display:flex;justify-content:space-between;margin-top:8px;text-align:center;font-size:11px}
.phase{width:60px;height:60px;border-radius:50%;margin-bottom:4px}

.photo-day{background:linear-gradient(135deg,#1b3f78,#5a8fd0 50%,#2a4f88)}
.feature{background:linear-gradient(160deg,#1c3552,#0d1a2b);color:var(--white)}
.feature h3{font-size:18px;color:#a9c8ec}
.feature p{font-size:12px;color:#d5dde6;margin-bottom:8px}
.newsletter p{font-size:13px;color:var(--muted);margin-bottom:18px}
.newsletter .field{background:var(--white);border:1px solid #cfd5db;height:40px;padding:10px 12px;color:var(--muted);font-size:12px}
.newsletter .btn{display:inline-block;margin-top:14px;background:var(--blue);color:var(--white);padding:8px 26px;font-size:16px}

.blog-item{display:flex;gap:14px;margin-bottom:18px;font-size:12px}
.blog-item .thumb{flex:0 0 70px;height:70px;border-radius:0}
.thumb-gal{background:linear-gradient(135deg,#e08a3a,#7b3d7a 60%,#2a2f6a)}
.video{height:230px;background:linear-gradient(180deg,#6f8fb4,#c5a880 70%,#3a3a3a);display:flex;align-items:center;justify-content:center}
.news p{font-size:12px;margin-bottom:12px;color:#e6eef7}
strong.read{color:var(--white);font-size:11px;white-space:nowrap}

/* footer */
.site-footer{height:284px;background:var(--footer);color:#b9bec6;position:relative}
.footer-main{display:flex;padding:44px 40px 0;font-size:12px}
.footer-brand{width:300px}
.footer-brand .brand{color:var(--white)}
.footer-brand .brand-dot{background:var(--white)}
.footer-col{width:150px;line-height:1.9}
.footer-social{margin-left:auto;text-align:center}
.footer-social h3{font-size:22px;font-weight:400;color:var(--white);line-height:1.3}
.circles{display:flex;gap:12px;justify-content:center;margin-top:16px}
.circles span{width:36px;height:36px;border-radius:50%;background:var(--white)}
.footer-bar{position:absolute;left:0;right:0;bottom:0;height:40px;background:var(--footer-bar);display:flex;align-items:center;padding:0 40px;font-size:11px}
.footer-bar nav{margin-left:auto;display:flex;gap:20px}
</style>
</head>
<body>
<header class="site-header">
  <a class="brand" href="#"><span class="brand-dot"></span>Pelmora Tours</a>
  <nav class="nav">
    <a class="active" href="#">Home</a><a href="#">Tours</a><a href="#">Astronomy Events</a><a href="#">Gallery</a><a href="#">Testimonials</a><a href="#">Contacts</a>
  </nav>
  <div class="header-meta">
    <span>info@pelmoratours.example</span><span>555-010-482</span>
    <a class="btn-sm" href="#">Login</a><a class="btn-sm" href="#">Register</a>
  </div>
</header>

<section class="hero" role="img" aria-label="Starry night sky over a calm Kimberley lake at dusk">
  <div class="hero-weather">
    <div>Kimberley, ZA<br>Partly sunny</div><strong>27°</strong>
    <div>Local<br>weather</div><strong>20°</strong>
  </div>
  <h1>Reserve your Astronomy tour</h1>
  <p>Ut wisi enim ad minim veniam nostrud exerci</p>
  <a class="btn" href="#">Reserve Now</a>
</section>

<section class="welcome">
  <div class="logo-mark"></div>
  <div class="logo-name">Pelmora Tours</div>
  <h2>Welcome to Pelmora Tours</h2>
  <p>Lorem ipsum dolor sit amet, consectetuer adipiscing elit, sed diam nonummy nibh euismod tincidunt ut laoreet dolore magna aliquam erat volutpat. Ut wisi enim ad minim veniam, quis nostrud exerci tation ullamcorper suscipit lobortis nisl ut aliquip ex ea commodo consequat. Duis autem vel eum iriure dolor in hendrerit in vulputate velit esse molestie consequat, vel illum dolore eu feugiat nulla facilisis.</p>
</section>

<main class="grid">
  <article class="tile t-dark">
    <h3>Astronomy Event</h3>
    <div class="calendar">
      <div class="month">MARCH 2015</div>
      <div class="days">
        <div>8<span>SUN</span></div><div>9<span>MON</span></div><div>10<span>TUE</span></div><div class="today">11<span>WED</span></div><div>12<span>THU</span></div><div>13<span>FRI</span></div><div>14<span>SAT</span></div>
      </div>
    </div>
    <div class="event-item">
      <div class="thumb thumb-night" role="img" aria-label="Night sky event photo"></div>
      <div>March 11<br><strong>Duis autem vel eum</strong><br>Hendrerit in vulputate velit esse molestie consequat illum.</div>
    </div>
    <a class="more" href="#">View More ›</a>
  </article>

  <article class="tile t-white">
    <h3>Telescope Rental</h3>
    <div class="rental">
      <div class="price-col">
        <div class="label">Mirror Telescope</div>
        <div class="label">Only</div>
        <div class="price">20€ <small>/ Per night</small></div>
        <p>Duis autem vel eum iriure dolor in hendrerit in vulputate velit esse molestie consequat, vel illum.</p>
      </div>
      <div class="product" role="img" aria-label="Portable amateur telescope on a tripod"></div>
    </div>
    <a class="more" href="#" style="color:var(--blue)">Reserve Now ›</a>
  </article>

  <article class="tile t-blue">
    <h3>Weather</h3>
    <div class="weather-now">
      <svg width="70" height="56" viewBox="0 0 70 56" aria-hidden="true"><circle cx="26" cy="24" r="16" fill="#f6c343"/><ellipse cx="42" cy="40" rx="24" ry="13" fill="#ffffff"/></svg>
      <div class="temp">27°</div>
      <div class="place">Kimberley, ZA<br>Local weather<br><strong style="font-size:22px">20°</strong></div>
    </div>
    <div class="moon">Moon Phases</div>
    <div class="phases">
      <div><div class="phase" style="background:linear-gradient(90deg,#1c2a3c 50%,#d7dde4 50%)"></div>1st</div>
      <div><div class="phase" style="background:#1c2a3c"></div>New</div>
      <div><div class="phase" style="background:linear-gradient(90deg,#d7dde4 50%,#1c2a3c 50%)"></div>3rd</div>
      <div><div class="phase" style="background:#d7dde4"></div>Full</div>
    </div>
    <a class="more" href="#">More Info ›</a>
  </article>

  <article class="tile t-blue photo-day">
    <h3>Picture Of The Day</h3>
    <div role="img" aria-label="Spiral galaxy photograph" style="position:absolute;inset:0;z-index:0"></div>
  </article>

  <article class="tile feature">
    <div role="img" aria-label="Stargazers with telescopes at dusk" style="height:70px"></div>
    <h3>Night sky adventure from Lake Kununurra</h3>
    <p>Ut wisi enim ad minim veniam quis nostrud exerci tation ullamcorper suscipit lobortis.</p>
    <p>Duis autem vel eum iriure dolor in hendrerit in vulputate velit esse.</p>
    <a class="more" href="#">See All ›</a>
  </article>

  <article class="tile t-grey newsletter">
    <h3>Newsletter</h3>
    <p>Receive latest sky event information, observing tips, and more from our monthly email newsletter.</p>
    <div class="field">Enter Email Address</div>
    <a class="btn" href="#">Sign Up ›</a>
  </article>

  <article class="tile t-blue">
    <h3>Blog</h3>
    <div class="blog-item"><div class="thumb thumb-gal" role="img" aria-label="Nebula photo"></div><div><strong>Duis autem vel eum</strong><br>Hendrerit in vulputate velit esse molestie.<br><strong class="read">READ STORY</strong></div></div>
    <div class="blog-item"><div class="thumb thumb-gal" role="img" aria-label="Nebula photo"></div><div><strong>Duis autem vel eum</strong><br>Hendrerit in vulputate velit esse molestie.<br><strong class="read">READ STORY</strong></div></div>
    <a class="more" href="#">View More ›</a>
  </article>

  <article class="tile t-white">
    <h3>Videos</h3>
    <div class="video" role="img" aria-label="Video of stargazers silhouetted at dusk">
      <svg width="70" height="70" viewBox="0 0 70 70" aria-hidden="true"><circle cx="35" cy="35" r="32" fill="rgba(0,0,0,.55)" stroke="#fff" stroke-width="3"/><path d="M28 22 L50 35 L28 48 Z" fill="#fff"/></svg>
    </div>
    <a class="more" href="#" style="color:var(--blue)">View More ›</a>
  </article>

  <article class="tile t-blue news">
    <h3>Latest News</h3>
    <p>Suscipit lobortis nisl ut aliquip ex ea commodo consequat. <strong class="read">READ STORY</strong></p>
    <p>Duis autem vel eum iriure dolor in hendrerit in vulputate. <strong class="read">READ STORY</strong></p>
    <p>Suscipit lobortis nisl ut aliquip ex ea commodo consequat. <strong class="read">READ STORY</strong></p>
    <p>Duis autem vel eum iriure dolor in hendrerit in vulputate. <strong class="read">READ STORY</strong></p>
    <a class="more" href="#">Read More ›</a>
  </article>
</main>

<footer class="site-footer">
  <div class="footer-main">
    <div class="footer-brand"><a class="brand" href="#"><span class="brand-dot"></span>Pelmora Tours</a></div>
    <div class="footer-col">About Us<br>Advertising<br>Contact Us<br>Terms of Use<br>Privacy Policy<br>Copyright Policy</div>
    <div class="footer-col">News<br>Observing<br>Photos<br>Videos<br>Blogs<br>Community</div>
    <div class="footer-social">
      <h3>Stay In Touch For<br>Latest Updates !</h3>
      <div class="circles"><span></span><span></span><span></span><span></span></div>
    </div>
  </div>
  <div class="footer-bar">
    <span>© Copyright 2015 Pelmora Tours . All Rights Reserved.</span>
    <nav><a href="#">Terms &amp; Services</a><a href="#">Privacy Policy</a><a href="#">Contact Us</a><a href="#">Client Center</a></nav>
  </div>
</footer>
</body>
</html>
```